Business Card Design Project

need some business cards with the logo provided. I am a manufacturing jeweller that make high end quality jewellery in silver, gold and platinum and some amazing colored stones and of course diamonds.
Updates

Project Deadline Extended
Reason: I didn't choose this specific deadline and not sure why it was so short. A team member of craft hive helped as i am not the best on computers. (-: (wasn't asked about the dead line)

Target Market(s)

Adults based between 20 to 60 and have budgets between $5000 - $100 000

Industry/Entity Type

Business

Colors

Designer to choose colors to be used in the design.

Requirements
Must have
• All in the front of business card
LOGO provided
My name: Marisol Kettering
Job: Manufacturing jeweller
Phone number: 047 215 3904
Email: ketmar@quillnet.example and the chatterbook logo
this all in the back:
description of what i do : Hand Made Jewellery
new designs, remodelling, bridal jewellery, pearl re-threading and repairs
PO Box 5817, Wyndell, 6418
Should not have
• Any diamond shapes or diamond rings or gemstones.

```html
<!DOCTYPE html>
<html lang="en">
<head>
<meta charset="utf-8">
<title>Marisol Kettering – Business Card</title>
<link href="https://fonts.googleapis.com/css2?family=Arimo:ital,wght@0,400;0,700;1,400&display=swap" rel="stylesheet">
<style>
  :root {
    --page: #ffffff;
    --card: #f4f1ee;
    --green: #7fb17a;
    --green-soft: #a9cfa0;
    --green-pale: #dcead5;
    --green-mid: #bcd9b2;
    --icon-top: #a8d07a;
    --icon-bottom: #6f9f4e;
    --ink: #1a1a1a;
    --white: #ffffff;
  }
  * { box-sizing: border-box; margin: 0; padding: 0; }
  html, body {
    width: 1200px; height: 347px; overflow: hidden;
    background: var(--page);
    font-family: "Arimo", Arial, sans-serif;
  }
  .canvas { position: relative; width: 1200px; height: 347px; }
  .card {
    position: absolute; top: 0; width: 590px; height: 341px;
    background: var(--card); overflow: hidden;
  }
  .card--front { left: 0; }
  .card--back { left: 610px; }

  .waves { position: absolute; left: 0; top: 0; }

  .logo-placeholder {
    position: absolute; left: 37px; top: 37px; width: 132px; height: 132px;
    border: 2px dashed var(--ink); border-radius: 50%;
    display: flex; align-items: center; justify-content: center;
    font-size: 27px; color: var(--ink); letter-spacing: 0.5px;
  }

  .identity { position: absolute; right: 48px; top: 74px; text-align: right; }
  .identity__name { font-size: 30px; font-weight: 700; color: var(--green); line-height: 1; margin-right: 27px; }
  .identity__role { font-size: 17px; color: var(--green-soft); line-height: 1; margin-top: 4px; }

  .contacts { position: absolute; right: 34px; top: 174px; list-style: none; }
  .contact { display: flex; align-items: center; justify-content: flex-end; height: 34px; margin-bottom: 8px; }
  .contact__text { font-size: 15px; color: var(--green-soft); margin-right: 12px; }
  .contact__text--social { color: var(--green); }
  .contact__icon {
    width: 34px; height: 34px; border-radius: 4px;
    background: linear-gradient(var(--icon-top), var(--icon-bottom));
    display: flex; align-items: center; justify-content: center;
  }

  .footer-band {
    position: absolute; left: 0; bottom: 0; width: 100%; height: 31px;
    background: var(--green);
    display: flex; align-items: center;
    font-size: 15px;
  }
  .footer-band--front { justify-content: flex-end; padding-right: 34px; font-style: italic; color: var(--ink); }
  .footer-band--back { justify-content: center; color: var(--white); }

  .stripe { position: absolute; left: 0; width: 100%; }
  .stripe--pale { top: 283px; height: 10px; background: var(--green-pale); }
  .stripe--mid { top: 293px; height: 17px; background: var(--green-mid); }

  .services { position: absolute; left: 0; top: 159px; width: 100%; text-align: center; }
  .services__title { font-size: 19px; font-weight: 700; color: var(--green); }
  .services__list { font-size: 15px; color: var(--green-soft); margin-top: 14px; }
</style>
</head>
<body>
<div class="canvas">

  <section class="card card--front">
    <svg class="waves" width="590" height="341" viewBox="0 0 590 341" aria-hidden="true">
      <path d="M0 207 C 130 265, 320 290, 590 280 L590 341 L0 341 Z" fill="var(--green-pale)"/>
      <path d="M0 234 C 90 285, 200 302, 320 296 C 420 290, 480 268, 530 272 C 560 275, 580 285, 590 292 L590 341 L0 341 Z" fill="var(--green-mid)"/>
    </svg>

    <div class="logo-placeholder">LOGO</div>

    <div class="identity">
      <p class="identity__name">Marisol Kettering</p>
      <p class="identity__role">manufacturing jeweller</p>
    </div>

    <ul class="contacts">
      <li class="contact">
        <span class="contact__text">047 215 3904</span>
        <span class="contact__icon">
          <svg width="22" height="22" viewBox="0 0 24 24" aria-hidden="true">
            <path d="M6.6 10.8c1.4 2.8 3.8 5.1 6.6 6.6l2.2-2.2c.3-.3.7-.4 1-.2 1.1.4 2.3.6 3.6.6.6 0 1 .4 1 1V20c0 .6-.4 1-1 1C10.6 21 3 13.4 3 4c0-.6.4-1 1-1h3.5c.6 0 1 .4 1 1 0 1.3.2 2.5.6 3.6.1.3 0 .7-.2 1z" fill="var(--white)"/>
          </svg>
        </span>
      </li>
      <li class="contact">
        <span class="contact__text">ketmar@quillnet.example</span>
        <span class="contact__icon">
          <svg width="24" height="18" viewBox="0 0 24 18" aria-hidden="true">
            <rect x="1" y="1" width="22" height="16" fill="none" stroke="var(--white)" stroke-width="1.6"/>
            <path d="M1 1 L12 10 L23 1" fill="none" stroke="var(--white)" stroke-width="1.6"/>
          </svg>
        </span>
      </li>
      <li class="contact">
        <span class="contact__text contact__text--social">chatterbook</span>
        <span class="contact__icon"></span>
      </li>
    </ul>

    <div class="footer-band footer-band--front">put your website here</div>
  </section>

  <section class="card card--back">
    <div class="services">
      <h1 class="services__title">Hand Made Jewellery</h1>
      <p class="services__list">new designs • remodelling • bridal jewellery • pearl re-threading • repairs</p>
    </div>
    <div class="stripe stripe--pale"></div>
    <div class="stripe stripe--mid"></div>
    <div class="footer-band footer-band--back">PO Box 5817, Wyndell, 6418</div>
  </section>

</div>
</body>
</html>
```